Lantern Sisters Ministries Logo/Business Card

Lantern Sisters are women full of God’s love and restorative grace, who have the desire to lead other women to embrace the beautiful creation that God intended them to be. Lantern Sisters walk together with other women alongside of God toward a life of healing, restoration and empowerment… through mentoring, spiritual guidance, temporary shelter, comprehensive care, and connections to a longer-term plan that leads to renewal and wholeness in Christ.

Lantern Sisters Ministries is an organization that embraces women and children whose lives have been affected by human trafficking, prison, foster care, homelessness, addictions, and other circumstances that prevent them from achieving their full potential in Christ Jesus. We believe that God has a unique plan and purpose for every individual. Through God’s transformational power and relationships with counselors, mentors, and others, anyone can break free from the chains and bondage of slavery, addictions and the strongholds of life.

We are just starting to brand our organization, and need both business cards and a logo. We do not have a logo yet, and would like design ideas. One of our young ladies (rescued from trafficking) has a vision of a logo with a crown with 3 ladies below/around it (representing healing, restoration, empowerment). Another lady has an idea of blending a crown, heart, and cross into the logo. We are open to creative suggestions.

Target Market(s)

Donations from churches, businesses, organizations and individuals with a passion for Trafficking and Justice

Industry/Entity Type

Business

Contact Information for Business Card

Lantern Sisters Ministries
women journeying side by side toward hope, renewal and new purpose (tag line - italics)

Card 1:
Harriet Pellow, Director
555.218.3074
harriet@lanternsistersministries.org
www.lanternsistersministries.org (optional)

Card 2:
Rebecca Thorsby, Director
555.637.4152
becca@lanternsistersministries.org

```html
<!DOCTYPE html>
<html lang="en">
<head>
<meta charset="utf-8">
<title>Lantern Sisters Ministries – Business Card</title>
<link rel="stylesheet" href="https://fonts.googleapis.com/css2?family=Great+Vibes&family=Montserrat:wght@400;500;600;700&display=swap">
<style>
  :root {
    --peach: #e9c6a3;
    --peach-light: #f3d9bd;
    --peach-deep: #dcb08a;
    --crimson: #9e1016;
    --crimson-dark: #740a0e;
    --ink: #141414;
    --white: #ffffff;
  }
  * { margin: 0; padding: 0; box-sizing: border-box; }
  html, body { width: 1200px; height: 704px; overflow: hidden; background: var(--peach); }
  .card {
    position: relative;
    width: 1200px;
    height: 704px;
    overflow: hidden;
    font-family: "Montserrat", sans-serif;
    color: var(--ink);
  }
  .card__backdrop {
    position: absolute;
    inset: 0;
    background:
      radial-gradient(ellipse 70% 80% at 22% 45%, var(--peach-light) 0%, var(--peach) 55%, var(--peach-deep) 100%);
  }
  .brand-mark {
    position: absolute;
    left: 112px;
    top: 180px;
    width: 300px;
    display: flex;
    align-items: center;
    gap: 14px;
    font-weight: 700;
    font-size: 30px;
    line-height: 1.2;
    color: var(--crimson);
    text-transform: uppercase;
  }
  .brand-mark__dot {
    flex: none;
    width: 30px;
    height: 30px;
    border-radius: 50%;
    background: var(--crimson);
  }
  .org-title {
    position: absolute;
    left: 440px;
    top: 72px;
    width: 720px;
    text-align: center;
    font-family: "Great Vibes", cursive;
    font-weight: 400;
    color: var(--white);
    font-size: 76px;
    line-height: 88px;
  }
  .person {
    position: absolute;
    left: 462px;
    top: 258px;
    font-size: 37px;
    letter-spacing: 0.2px;
    white-space: nowrap;
  }
  .person__name { font-weight: 700; }
  .person__role { font-weight: 400; }
  .contacts {
    position: absolute;
    left: 460px;
    top: 344px;
    list-style: none;
  }
  .contacts__item {
    display: flex;
    align-items: center;
    gap: 16px;
    font-weight: 500;
    font-size: 30px;
    height: 50px;
    white-space: nowrap;
  }
  .contacts__item--phone { font-size: 34px; font-weight: 600; margin-bottom: 2px; }
  .contacts__bullet {
    flex: none;
    width: 24px;
    height: 24px;
    border-radius: 50%;
    background: var(--crimson);
  }
  .tagline {
    position: absolute;
    left: 0;
    top: 564px;
    width: 1200px;
    height: 48px;
    background: linear-gradient(90deg, var(--crimson-dark), var(--crimson) 50%, var(--crimson-dark));
    color: var(--white);
    font-size: 25px;
    font-weight: 400;
    line-height: 48px;
    padding-left: 112px;
    white-space: nowrap;
  }
</style>
</head>
<body>
  <main class="card">
    <div class="card__backdrop" role="img" aria-label="Warm peach sunburst of soft light rays radiating behind the ministry emblem"></div>

    <div class="brand-mark">
      <span class="brand-mark__dot"></span>
      <span class="brand-mark__name">Lantern Sisters Ministries</span>
    </div>

    <h1 class="org-title">Lantern<br>Sisters Ministries</h1>

    <p class="person"><span class="person__name">REBECCA THORSBY - </span><span class="person__role">DIRECTOR</span></p>

    <ul class="contacts">
      <li class="contacts__item contacts__item--phone"><span class="contacts__bullet"></span>555.637.4152</li>
      <li class="contacts__item"><span class="contacts__bullet"></span>becca@lanternsistersministries.org</li>
      <li class="contacts__item"><span class="contacts__bullet"></span>www.lanternsistersministries.org</li>
    </ul>

    <p class="tagline">women journeying side by side toward hope, renewal and new purpose</p>
  </main>
</body>
</html>
```